International Clinical Software Company needs a new business card design

We are looking for a new business card design for our company that has recently expanded into the UK market, making us a multinational company.
After having rebranded our website and produced a new style guide, we are looking for a business card that is creative and attention grabbing, while being consistent with the style and colour scheme used on the new website, www.pennick.care
We produce care management technology for the aged care market, but the main aspect we aim to communicate is the human element of our software, and the way it assists in providing better care for aged people, and stronger relationships between aged people and the staff that care for them.
Our current business card is a dark green with gold text, which makes the text quite difficult to read, not very aesthetically appealing and the colour scheme looks quite dated.
We would like something fresh and modern, that can still be colourful but doesn't use large blocks of dark colour, and uses the colours within our logo.
Something tying in with the leaves that are used in our logo could work quite nicely, along with the Autumn/Fall colours of soft greens, yellows and reds (also in our existing logo). However also happy to look at fresh, completely out of the box ideas we may not have yet considered.
Target Market(s)
The people that receive this business card work in the aged card or health industry and are either corporate/management level staff or clinical (Registered Nurses, care workers etc.)
Industry/Entity Type
Health Product
Contact Information for Business Card
Company Name - Pennick Care
Company locations: United Kingdom, Australia, New Zealand
Staff Details:
Staff name: Dermot Marlow
Staff job title: Executive Chairman
Staff email: d.marlow@pennick.care
Office phone number: 01632 960481
Other font styles liked:
- Calibri
Requirements
Must have
- Must include the Pennick Care brand name in it's current font
- Must include logo (3 leaves in gold circle)
- Must include Business Card Details
Nice to have
- Elements of gold
- White space
- Something autumn themed but not too cliched
Should not have
- No blue - used by a major competitor and we would like to differentiate from them
- Large blocks of dark green colour (the green that appears in our leaves on the logo on our current business card is the background colour and it is far too dark)

```html
<!DOCTYPE html>
<html lang="en">
<head>
<meta charset="utf-8">
<title>Pennick Care business card</title>
<link rel="stylesheet" href="https://fonts.googleapis.com/css2?family=Arimo:wght@400;700&display=swap">
<style>
  :root {
    --page-bg: #e9e6e0;
    --card-bg: #ffffff;
    --gold: #b3a47e;
    --magenta: #c2185f;
    --grey: #6b6b6b;
    --icon: #8a8580;
  }
  * { margin: 0; padding: 0; box-sizing: border-box; }
  html, body {
    width: 1200px;
    height: 950px;
    overflow: hidden;
    background: var(--page-bg);
    font-family: "Arimo", Arial, sans-serif;
  }
  .business-card {
    position: absolute;
    left: 110px;
    top: 195px;
    width: 980px;
    height: 560px;
    background: var(--card-bg);
    overflow: hidden;
    box-shadow: 0 10px 30px rgba(0,0,0,0.18);
  }
  .brand-name {
    position: absolute;
    left: 470px;
    top: 96px;
    font-size: 46px;
    font-weight: 400;
    color: var(--gold);
    letter-spacing: 1px;
    white-space: nowrap;
  }
  .locations {
    position: absolute;
    right: 86px;
    top: 232px;
    text-align: right;
    font-size: 24px;
    line-height: 1.3;
    color: var(--grey);
    list-style: none;
  }
  .person {
    position: absolute;
    left: 96px;
    top: 208px;
  }
  .person-name {
    font-size: 31px;
    font-weight: 700;
    color: var(--gold);
  }
  .person-title {
    margin-top: 4px;
    font-size: 24px;
    color: var(--magenta);
  }
  .edge-tab {
    position: absolute;
    left: -48px;
    top: 262px;
    width: 96px;
    height: 96px;
    border-radius: 50%;
    background: var(--gold);
  }
  .contacts {
    position: absolute;
    left: 96px;
    top: 420px;
    list-style: none;
    font-size: 24px;
    color: var(--grey);
    line-height: 1.35;
  }
  .contacts li {
    display: flex;
    align-items: center;
    gap: 10px;
  }
  .contacts svg {
    width: 20px;
    height: 20px;
    fill: var(--icon);
    flex: none;
  }
</style>
</head>
<body>
  <article class="business-card">
    <p class="brand-name">Pennick Care</p>

    <ul class="locations">
      <li>United Kingdom</li>
      <li>Australia</li>
      <li>New Zealand</li>
    </ul>

    <span class="edge-tab"></span>

    <div class="person">
      <h1 class="person-name">Dermot Marlow</h1>
      <p class="person-title">Executive Chairman</p>
    </div>

    <ul class="contacts">
      <li>
        <svg viewBox="0 0 20 20" aria-hidden="true"><path d="M2 7c0-2 3-4 8-4s8 2 8 4v2h-4V7.5c-1-.6-2.4-.9-4-.9s-3 .3-4 .9V9H2z"/><path d="M5 10h10l2 6H3z"/><circle cx="10" cy="13" r="1.8" fill="#fff"/></svg>
        <span>01632 960481</span>
      </li>
      <li>
        <svg viewBox="0 0 20 20" aria-hidden="true"><path d="M2 5h16v10H2z"/><path d="M2 5l8 6 8-6" fill="none" stroke="#fff" stroke-width="1.5"/></svg>
        <span>d.marlow@pennick.care</span>
      </li>
      <li>
        <svg viewBox="0 0 20 20" aria-hidden="true"><circle cx="10" cy="10" r="8"/><path d="M2 10h16M10 2c3 3 3 13 0 16M10 2c-3 3-3 13 0 16" fill="none" stroke="#fff" stroke-width="1.2"/></svg>
        <span>www.pennick.care</span>
      </li>
    </ul>
  </article>
</body>
</html>
```